Manufacturing company needs new business card.

I need a unique Business Card that will truly stand out. Nothing too busy. Simple is good, right? Not looking for a standard design either. No cookie cutter layout. I am just looking for something interesting and a bit different. Does't have to completely off the wall crazy, just not your run of the mill business card. Clean and modern with a touch of industrial.

Target Market(s)

Air conditioning industry, Architects, builders.

Industry/Entity Type

Business

Contact Information for Business Card

Details to be included on card are:

Peter Vance
Managing Director

T: 1300 847 519
M: 0428 593 174
W: www.brenvaleworks.com.au
E: peter.vance@brenvaleworks.com.au
A: 58 Harwick Lane, Sydney NSW 2000

Font styles to use
Sans Serif

Colors
0355a3
848484
fbfbfb

Requirements
Must have
• Card design must be landscape.

```html
<!DOCTYPE html>
<html lang="en">
<head>
<meta charset="utf-8">
<title>Brenvale Works – Business Card</title>
<link href="https://fonts.googleapis.com/css2?family=Lato:wght@300;400;700&display=swap" rel="stylesheet">
<style>
  :root {
    --brand-blue: #0355a3;
    --band-blue: #2152a3;
    --brand-grey: #848484;
    --paper: #fbfbfb;
    --ink: #555555;
    --backdrop: #2e2e2e;
  }
  * { margin: 0; padding: 0; box-sizing: border-box; }
  html, body {
    width: 1200px; height: 880px; overflow: hidden;
    background: var(--backdrop);
    font-family: 'Lato', Arial, sans-serif;
  }
  .sheet {
    width: 1200px; height: 880px;
    display: flex; flex-direction: column; align-items: center; justify-content: center;
    gap: 30px;
  }
  .card {
    position: relative;
    width: 640px; height: 391px;
    background: var(--paper);
    overflow: hidden;
    box-shadow: 0 6px 18px rgba(0,0,0,.45);
  }

  /* Front */
  .front-brand {
    position: absolute; left: 110px; top: 140px;
    display: flex; align-items: center; gap: 16px;
  }
  .brand-square {
    width: 46px; height: 46px; background: var(--brand-blue);
  }
  .brand-name {
    font-weight: 700; color: var(--brand-blue);
    font-size: 38px; letter-spacing: -0.5px; line-height: 1;
  }
  .brand-region {
    display: block; font-weight: 700; color: var(--brand-blue);
    font-size: 15px; letter-spacing: 9px; margin-top: 8px;
  }
  .front-rule {
    position: absolute; left: 172px; top: 232px;
    width: 150px; height: 2px; background: var(--brand-grey);
  }
  .front-web {
    position: absolute; left: 172px; top: 252px;
    font-size: 15px; color: var(--ink); letter-spacing: .2px;
  }
  .front-web span { color: var(--brand-blue); }

  /* Back */
  .band { position: absolute; inset: 0; }
  .back-square {
    position: absolute; left: 38px; top: 62px;
    width: 44px; height: 44px; background: #ffffff;
  }
  .back-brand {
    position: absolute; left: 196px; top: 48px;
  }
  .back-brand .brand-name { font-size: 40px; }
  .back-rule {
    position: absolute; left: 196px; top: 122px;
    width: 150px; height: 2px; background: var(--brand-grey);
  }
  .person {
    position: absolute; left: 220px; top: 150px;
    display: flex; align-items: baseline; gap: 10px;
  }
  .person-name {
    font-weight: 700; color: var(--brand-blue); font-size: 21px; text-transform: uppercase;
  }
  .person-title {
    color: var(--brand-grey); font-size: 16px;
    border-left: 1px solid var(--brand-grey); padding-left: 10px;
  }
  .contacts {
    position: absolute; left: 220px; top: 198px;
    list-style: none;
  }
  .contacts li {
    display: flex; align-items: center; gap: 10px;
    font-size: 15px; color: var(--ink); height: 27px;
  }
  .contact-icon {
    width: 20px; height: 20px; background: var(--band-blue);
    display: flex; align-items: center; justify-content: center; flex: none;
  }
</style>
</head>
<body>
<main class="sheet">

  <section class="card card-front" aria-label="Card front">
    <div class="front-brand">
      <div class="brand-square"></div>
      <div class="brand-name">Brenvale Works<span class="brand-region">AUSTRALIA</span></div>
    </div>
    <div class="front-rule"></div>
    <p class="front-web">www.<span>brenvaleworks</span>.com.au</p>
  </section>

  <section class="card card-back" aria-label="Card back">
    <svg class="band" width="640" height="391" viewBox="0 0 640 391">
      <polygon points="0,0 96,0 196,391 0,391" fill="var(--band-blue)"/>
      <line x1="104" y1="0" x2="204" y2="391" stroke="var(--brand-grey)" stroke-width="2"/>
    </svg>
    <div class="back-square"></div>
    <div class="back-brand">
      <div class="brand-name">Brenvale Works<span class="brand-region">AUSTRALIA</span></div>
    </div>
    <div class="back-rule"></div>

    <div class="person">
      <span class="person-name">Peter Vance</span>
      <span class="person-title">Managing Director</span>
    </div>

    <ul class="contacts">
      <li>
        <span class="contact-icon">
          <svg width="12" height="12" viewBox="0 0 12 12"><path d="M2 1h3l1 3-1.5 1a7 7 0 0 0 2.5 2.5L8 6l3 1v3a1 1 0 0 1-1 1A9 9 0 0 1 1 2a1 1 0 0 1 1-1z" fill="#fff"/></svg>
        </span>1300 847 519
      </li>
      <li>
        <span class="contact-icon">
          <svg width="12" height="12" viewBox="0 0 12 12"><rect x="3" y="0.5" width="6" height="11" rx="1" fill="none" stroke="#fff" stroke-width="1.2"/><circle cx="6" cy="9.5" r=".8" fill="#fff"/></svg>
        </span>0428 593 174
      </li>
      <li>
        <span class="contact-icon">
          <svg width="12" height="12" viewBox="0 0 12 12"><rect x="0.7" y="2.5" width="10.6" height="7" fill="none" stroke="#fff" stroke-width="1.2"/><path d="M1 3l5 4 5-4" fill="none" stroke="#fff" stroke-width="1.2"/></svg>
        </span>peter.vance@brenvaleworks.com.au
      </li>
      <li>
        <span class="contact-icon">
          <svg width="12" height="12" viewBox="0 0 12 12"><circle cx="6" cy="6" r="5" fill="none" stroke="#fff" stroke-width="1.1"/><ellipse cx="6" cy="6" rx="2.2" ry="5" fill="none" stroke="#fff" stroke-width="1"/><line x1="1" y1="6" x2="11" y2="6" stroke="#fff" stroke-width="1"/></svg>
        </span>www.brenvaleworks.com.au
      </li>
      <li>
        <span class="contact-icon">
          <svg width="12" height="12" viewBox="0 0 12 12"><path d="M6 11.5S2 7 2 4.5a4 4 0 0 1 8 0C10 7 6 11.5 6 11.5z" fill="#fff"/><circle cx="6" cy="4.5" r="1.4" fill="var(--band-blue)"/></svg>
        </span>58 Harwick Lane, Sydney NSW 2000
      </li>
    </ul>
  </section>

</main>
</body>
</html>
```